Evaporative Air Conditioning Summer Service

Would like to design a flyer to send out in an email to existing clients to promote a Pre-summer service for Evaporative Air Conditioners
Cost will be $110.00 inc gst
Tasks included in service are
- Inspection and clean of pads
- Inspection and check float valve, water pump, fan, motor, bearings, drain
- Clean basin
- Supply of bacterial tablet
- Inspect overall condition of unit
- Any repairs if required will be quoted
Please see files attached of a previous very basic flyer I have used for installation and replacement unit costs. This has current contact information
Have also uploaded company logo for use.
Thanks
Plumbing

```html
<!DOCTYPE html>
<html lang="en">
<head>
<meta charset="utf-8">
<title>Pre-Summer Evaporative Air Conditioner Service</title>
<link href="https://fonts.googleapis.com/css2?family=Montserrat:wght@400;600;700;800&family=Oswald:wght@500;700&display=swap" rel="stylesheet">
<style>
:root{
  --page:#e4e4e4;
  --white:#ffffff;
  --navy:#16254d;
  --deep:#0f1b3a;
  --blue:#1f63c6;
  --sky:#2d86e6;
  --orange:#f4a11d;
  --orange-dark:#e07c10;
  --photo-a:#c9d3df;
  --photo-b:#8a9cb3;
}
*{box-sizing:border-box;margin:0;padding:0}
html,body{width:1200px;height:2508px;overflow:hidden;background:var(--page)}
body{font-family:"Montserrat",Arial,sans-serif;position:relative}
.flyer{position:absolute;left:40px;top:462px;width:1120px;height:1584px;background:var(--white);overflow:hidden;box-shadow:0 6px 24px rgba(0,0,0,.12)}
.hero-photo{position:absolute;right:0;top:0;width:560px;height:490px;background:linear-gradient(160deg,#f3f5f8 0%,var(--photo-a) 45%,#3a4f7a 100%)}
.brand{position:absolute;left:60px;top:60px;display:flex;align-items:center;gap:16px}
.brand-mark{width:46px;height:46px;background:var(--orange);border-radius:50%}
.brand-name{font-weight:800;font-size:34px;color:var(--navy);line-height:1;letter-spacing:.5px}
.headline{position:absolute;left:60px;top:175px;width:540px;font-family:"Oswald",sans-serif;font-weight:700}
.headline span{display:block}
.headline .pre{font-size:50px;color:var(--orange);line-height:1.05}
.headline .for{font-size:62px;color:var(--navy);line-height:1.05}
.headline .evap{font-size:100px;color:var(--blue);line-height:1;letter-spacing:-1px}
.headline .ac{font-weight:500;font-size:44px;color:var(--navy);line-height:1.15;letter-spacing:1px}
.intro-band{position:absolute;left:0;top:500px;width:640px;height:130px;background:linear-gradient(90deg,var(--blue),var(--sky));padding:0 36px 0 60px;display:flex;align-items:center;color:var(--white);font-size:23px;font-weight:600;line-height:1.38}
.price{position:absolute;left:680px;top:510px;display:flex;align-items:stretch;height:110px}
.price-label{padding:10px 18px 0 0;font-family:"Oswald",sans-serif;font-weight:700;color:var(--navy);line-height:1}
.price-label .cost{font-size:56px;display:block}
.price-label .will{font-size:26px;display:block;margin-top:4px}
.price-box{background:linear-gradient(180deg,var(--orange),var(--orange-dark));color:var(--navy);padding:8px 20px;font-family:"Oswald",sans-serif;font-weight:700;text-align:center;line-height:1}
.price-box .amount{font-size:58px;display:block}
.price-box .gst{font-size:30px;display:block;margin-top:4px}
.tasks{position:absolute;left:0;top:670px;width:1120px;height:650px;background:linear-gradient(180deg,var(--navy),var(--deep))}
.tasks-title{position:absolute;left:50%;top:-4px;transform:translateX(-50%);background:var(--navy);border:3px solid var(--sky);border-radius:40px;padding:14px 56px;color:var(--white);font-weight:700;font-size:36px;white-space:nowrap}
.task-grid{position:absolute;left:110px;top:105px;width:900px;display:grid;grid-template-columns:repeat(3,260px);column-gap:60px;row-gap:30px}
.task{text-align:center;color:var(--white)}
.task-photo{width:240px;height:150px;margin:0 auto;border:4px solid var(--white);background:linear-gradient(135deg,var(--photo-a),var(--photo-b))}
.task-text{margin-top:12px;font-size:20px;font-weight:600;line-height:1.3;min-height:78px}
.footer-unit{position:absolute;left:30px;top:1320px;width:470px;height:264px;background:linear-gradient(180deg,#f6f7f9,#c3cad4)}
.contact{position:absolute;left:500px;top:1350px;width:620px;height:234px;background:linear-gradient(90deg,var(--blue),var(--sky));padding:22px 34px;color:var(--white)}
.contact-line{display:flex;align-items:center;gap:12px;font-weight:600;line-height:1.3;margin-top:6px}
.contact-line svg{flex:none}
.call-label{font-size:20px;font-weight:600;color:var(--orange);margin-left:42px}
.phone{font-size:38px;font-weight:800;margin-top:0}
.email{font-size:21px}
.abn{font-size:22px;font-weight:700}
.fine-print{font-size:11px;margin-top:12px;line-height:1.35;opacity:.9}
</style>
</head>
<body>
<main class="flyer">
  <div class="hero-photo" role="img" aria-label="Technician in cap and navy uniform servicing a wall mounted air conditioner"></div>

  <div class="brand">
    <span class="brand-mark"></span>
    <span class="brand-name">SUMMIT GAS &amp; PLUMBING</span>
  </div>

  <h1 class="headline">
    <span class="pre">PRE-SUMMER</span>
    <span class="for">SERVICE FOR</span>
    <span class="evap">EVAPORATIVE</span>
    <span class="ac">AIR CONDITIONERS</span>
  </h1>

  <p class="intro-band">We are a professional group of plumbers and gas fitters servicing the domestic, commercial and industrial sectors.</p>

  <div class="price">
    <div class="price-label"><span class="cost">COST</span><span class="will">WILL BE</span></div>
    <div class="price-box"><span class="amount">$110.00</span><span class="gst">INC GST</span></div>
  </div>

  <section class="tasks">
    <h2 class="tasks-title">Tasks included in service are</h2>
    <div class="task-grid">
      <div class="task"><div class="task-photo" role="img" aria-label="Cooler pads being inspected and cleaned"></div><p class="task-text">Inspection and clean of pads</p></div>
      <div class="task"><div class="task-photo" role="img" aria-label="Technician checking pump and motor"></div><p class="task-text">Inspection and check float valve, water pump, fan, motor, bearings, drain</p></div>
      <div class="task"><div class="task-photo" role="img" aria-label="Basin being cleaned"></div><p class="task-text">Clean basin</p></div>
      <div class="task"><div class="task-photo" role="img" aria-label="Bacterial tablet in gloved hand"></div><p class="task-text">Supply of bacterial tablet</p></div>
      <div class="task"><div class="task-photo" role="img" aria-label="Technician inspecting an outdoor unit"></div><p class="task-text">Inspect overall condition of unit</p></div>
      <div class="task"><div class="task-photo" role="img" aria-label="Repair work on an air conditioner"></div><p class="task-text">Any repairs if required will be quoted</p></div>
    </div>
  </section>

  <div class="footer-unit" role="img" aria-label="Outdoor air conditioning unit beside an indoor split unit"></div>

  <div class="contact">
    <p class="call-label">Call us today</p>
    <p class="contact-line phone">
      <svg width="30" height="30" viewBox="0 0 24 24"><circle cx="12" cy="12" r="12" fill="#f4a11d"/><path d="M8 6l2 0 1 3-1.5 1a7 7 0 0 0 4.5 4.5l1-1.5 3 1 0 2c0 1-1 2-2 2A11 11 0 0 1 6 8c0-1 1-2 2-2z" fill="#fff"/></svg>
      +61 400 555 218</p>
    <p class="contact-line email">
      <svg width="30" height="26" viewBox="0 0 24 24"><circle cx="12" cy="12" r="12" fill="#f4a11d"/><rect x="6" y="8" width="12" height="8" fill="#fff"/><path d="M6 8l6 5 6-5" stroke="#f4a11d" stroke-width="1.4" fill="none"/></svg>
      admin@summitgasplumbing.com.au</p>
    <p class="contact-line abn">
      <svg width="30" height="26" viewBox="0 0 24 24"><circle cx="12" cy="12" r="12" fill="#f4a11d"/><path d="M12 5a4.5 4.5 0 0 0-4.5 4.5C7.5 13 12 19 12 19s4.5-6 4.5-9.5A4.5 4.5 0 0 0 12 5z" fill="#fff"/><circle cx="12" cy="9.5" r="1.6" fill="#f4a11d"/></svg>
      ABN 12 345 678 901</p>
    <p class="fine-print">* Service bookings are subject to availability. Parts and extra labour required for repairs will be quoted before any work.</p>
  </div>
</main>
</body>
</html>
```